Company Website for an IT business called "BRIGHT HARBOR"

Complete website creation with text and graphics.
We need :
- modern and creative design for our IT company
- Content management system to edit text later on
- Integrate third party content from partner company
- Contact form (transfer by email)
Updates

Target Market(s)

Small and medium business
private customers

Industry/Entity Type

Information Technology

Coding

Coded - Design and coding required

Number of Pages Required

1 page

Font styles to use
Sans Serif

Requirements
Must have
• Contact form
Link to legal information
Link to data protection (GDPR)
Link to website owner declaration
Nice to have
• Fresh and creative graphics for IT business

```html
<!DOCTYPE html>
<html lang="en">
<head>
<meta charset="utf-8">
<title>Bright Harbor – IT Solutions</title>
<link rel="stylesheet" href="https://fonts.googleapis.com/css2?family=Raleway:wght@400;500;600;700&family=Playfair+Display:wght@400&family=Mulish:wght@400;600;700&display=swap">
<style>
:root{
  --blue:#0a8bc8;
  --bright:#1da1ee;
  --royal:#0a66cc;
  --navy:#0c2d5e;
  --teal:#0ab4cc;
  --ink:#1f2326;
  --text:#4a5157;
  --pale:#f1f5f8;
  --line:#dde3e8;
  --dark:#151c22;
  --deep:#134260;
  --foot:#f3f6f9;
  --white:#ffffff;
}
*{margin:0;padding:0;box-sizing:border-box}
html,body{width:1200px;height:3887px;overflow:hidden}
body{position:relative;background:var(--white);font-family:'Mulish',sans-serif;color:var(--text)}
.abs{position:absolute}
.serif{font-family:'Playfair Display',serif;font-weight:400}
.head{font-family:'Raleway',sans-serif}
.btn{position:absolute;background:var(--blue);color:var(--white);font:700 13px 'Mulish',sans-serif;display:flex;align-items:center;justify-content:center;letter-spacing:.2px}

/* hero */
.hero{left:0;top:0;width:1200px;height:614px;background:linear-gradient(100deg,#0f1c27 0%,#1c2b38 45%,#2b3a46 100%)}
.hero-photo{left:420px;top:55px;width:640px;height:540px}
.brand{left:113px;top:8px;display:flex;align-items:center;gap:10px;color:var(--white);font:700 19px 'Raleway',sans-serif;letter-spacing:1px}
.brand-mark{width:26px;height:26px;background:var(--bright)}
.nav{left:729px;top:27px;display:flex;gap:0;font:600 12px 'Mulish',sans-serif;color:var(--white)}
.nav span{position:absolute;white-space:nowrap}
.hero-kicker{left:113px;top:180px;color:var(--white);font-size:22px}
.hero-title{left:113px;top:202px;color:var(--white);font:700 58px 'Playfair Display',serif;line-height:1}
.hero-title b{color:var(--bright);font-weight:700}
.hero-sub{left:113px;top:258px;color:var(--white);font-size:54px;line-height:1.1}
.hero-copy{left:113px;top:322px;width:430px;color:#e6ecf0;font-size:14px;line-height:22px}
.dots{left:111px;top:584px;display:flex;gap:6px}
.dots i{width:8px;height:8px;border-radius:50%;background:var(--white)}
.dots i:first-child{background:var(--bright)}
.accent-line{left:1086px;top:596px;width:3px;height:56px;background:var(--blue)}

/* welcome */
.welcome-photo{left:53px;top:679px;width:551px;height:395px}
.label{color:var(--blue);font-size:19px}
.h2{font:600 46px 'Raleway',sans-serif;color:var(--ink);line-height:1}
.para{font-size:15px;line-height:24px;color:var(--text)}

/* services */
.center{left:0;width:1200px;text-align:center}
.card{position:absolute;width:306px;height:269px;padding:27px 18px 0}
.card svg{width:48px;height:48px;display:block}
.card h3{margin-top:28px;font:500 22px 'Raleway',sans-serif;color:var(--ink)}
.card p{margin-top:12px;font-size:13px;line-height:20px}
.c-blue{background:var(--blue)}
.c-pale{background:var(--pale)}
.c-line{background:var(--white);border:1px solid var(--line)}
.c-navy{background:var(--navy)}
.c-teal{background:var(--teal)}
.c-blue h3,.c-blue p,.c-navy h3,.c-teal h3,.c-teal p{color:var(--white)}
.c-navy p{color:#c9d6e6}

/* consulting */
.consult{left:0;top:1853px;width:1200px;height:457px;background:var(--dark)}

/* testimonials */
.quote{position:absolute;width:474px;height:265px;padding:33px 26px 0}
.quote p{margin-top:26px;font-size:13.5px;line-height:22px}
.quote h4{margin-top:20px;font:700 15px 'Mulish',sans-serif}
.quote small{display:block;font-size:12px;margin-top:1px}
.q-blue{background:var(--blue);color:var(--white)}
.q-blue p{color:#e4f2fa}
.q-pale{background:var(--pale);color:var(--ink)}
.q-line{background:var(--white);border:1px solid var(--line);color:var(--ink)}
.q-royal{background:var(--royal);color:var(--white)}
.q-royal p{color:#e4eefa}

/* contact */
.contact{left:0;top:3095px;width:1200px;height:407px;background:var(--deep)}
.field{position:absolute;background:var(--white);border:1px solid #cfd8de;font-size:12px;color:#7a848b;padding:12px 16px}

/* footer */
.footer{left:0;top:3502px;width:1200px;height:385px;background:var(--foot)}
.f-head{position:absolute;top:3560px;font-size:19px;color:var(--ink)}
.f-list{position:absolute;top:3596px;font-size:12px;line-height:28.7px;color:var(--text);list-style:none}
.f-contact{position:absolute;left:644px;font-size:12px;line-height:18px;color:var(--text);display:flex;gap:6px}
.social{position:absolute;left:988px;display:flex;align-items:center;gap:10px;font-size:12px;color:var(--text)}
.social i{width:36px;height:36px;border-radius:50%;background:var(--white);border:1px solid var(--line)}
</style>
</head>
<body>

<!-- HERO -->
<section class="abs hero"></section>
<svg class="abs hero-photo" viewBox="0 0 640 540" role="img" aria-label="Photo of a team working on laptops, framed in slanted panels">
  <defs>
    <linearGradient id="hp" x1="0" y1="0" x2="1" y2="1">
      <stop offset="0" stop-color="#c9b8a4"/><stop offset=".5" stop-color="#7d7f86"/><stop offset="1" stop-color="#d8dde2"/>
    </linearGradient>
  </defs>
  <polygon points="25,22 520,22 420,300 220,300 120,540 40,540 180,200 25,200" fill="#5a6670" opacity=".55"/>
  <polygon points="160,22 590,0 270,540 40,540" fill="url(#hp)" opacity=".85"/>
  <rect x="290" y="360" width="338" height="92" fill="#e7ebee" opacity=".8"/>
  <line x1="560" y1="0" x2="230" y2="540" stroke="#1a2530" stroke-width="4"/>
</svg>
<div class="abs brand"><span class="brand-mark"></span>BRIGHT HARBOR</div>
<nav class="abs nav">
  <span style="left:0;color:var(--bright)">HOME</span>
  <span style="left:75px">COMPANY</span>
  <span style="left:175px">OUR SERVICES</span>
  <span style="left:302px">CONTACT</span>
</nav>
<div class="abs serif hero-kicker">COMPLEX</div>
<h1 class="abs hero-title">IT <b>SOLUTION</b></h1>
<div class="abs serif hero-sub">For Your Business</div>
<p class="abs hero-copy">Aliquam fringilla aliquam ex sit amet elementum. Proin bibendum sollicitudin feugiat curabitur.</p>
<div class="btn" style="left:110px;top:382px;width:153px;height:45px">GET IN TOUCH</div>
<div class="abs dots"><i></i><i></i><i></i></div>
<div class="abs accent-line"></div>

<!-- WELCOME -->
<svg class="abs welcome-photo" viewBox="0 0 551 395" role="img" aria-label="Photo of colleagues reviewing documents at a desk, cut into a tilted diamond">
  <defs>
    <linearGradient id="wp" x1="0" y1="0" x2="1" y2="1">
      <stop offset="0" stop-color="#e9ecef"/><stop offset=".5" stop-color="#8c8f95"/><stop offset="1" stop-color="#d4d7db"/>
    </linearGradient>
  </defs>
  <polygon points="60,230 400,0 480,240 290,395" fill="url(#wp)"/>
  <line x1="300" y1="30" x2="230" y2="350" stroke="#fff" stroke-width="3"/>
  <line x1="380" y1="60" x2="300" y2="395" stroke="#fff" stroke-width="3"/>
</svg>
<div class="abs serif label" style="left:613px;top:741px">Welcome To</div>
<h2 class="abs h2" style="left:613px;top:769px">BRIGHT HARBOR</h2>
<p class="abs para" style="left:613px;top:824px;width:475px">Nemo enim ipsam voluptatem quia voluptas sit aspernatur aut odit aut fugit, sed quia consequuntur magni dolores eos qui ratione voluptatem sequi nesciunt. Neque porro quisquam est, qui dolorem ipsum quia dolor sit amet, consectetur, adipisci velit, sed quia non numquam</p>
<div class="btn" style="left:613px;top:964px;width:126px;height:42px">READ MORE</div>

<!-- SERVICES -->
<div class="abs center serif label" style="top:1134px">Services</div>
<h2 class="abs center h2" style="top:1160px">WHAT WE DO</h2>

<article class="card c-blue" style="left:113px;top:1222px">
  <svg viewBox="0 0 48 48" fill="none" stroke="#fff" stroke-width="2"><rect x="16" y="4" width="26" height="18" rx="2"/><path d="M4 30h8v12H4zM12 32h10l8 4 12-6-4 10-16 2-10-2"/></svg>
  <h3>Software Installation</h3>
  <p>Nor again is there anyone who loves or pursues or desires to obtain pain of itself because it is pain, but because occasionally circumstances occur in which toil...</p>
</article>
<article class="card c-pale" style="left:447px;top:1222px">
  <svg viewBox="0 0 48 48" fill="none" stroke="#1f2326" stroke-width="2"><circle cx="24" cy="24" r="18"/><circle cx="24" cy="24" r="6" fill="#1f2326"/><circle cx="24" cy="6" r="3" fill="#1f2326"/><circle cx="8" cy="32" r="3" fill="#1f2326"/><circle cx="40" cy="32" r="3" fill="#1f2326"/></svg>
  <h3>Cloud Services</h3>
  <p>Nor again is there anyone who loves or pursues or desires to obtain pain of itself because it is pain, but because occasionally circumstances occur in which toil...</p>
</article>
<article class="card c-line" style="left:780px;top:1222px">
  <svg viewBox="0 0 48 48" fill="#1f2326"><rect x="4" y="6" width="40" height="28" rx="2"/><rect x="18" y="36" width="12" height="4"/><rect x="12" y="40" width="24" height="4"/><path d="M24 12l6 8h-4v8h-4v-8h-4z" fill="#fff"/></svg>
  <h3>Boost up your System</h3>
  <p>Nor again is there anyone who loves or pursues or desires to obtain pain of itself because it is pain, but because occasionally circumstances occur in which toil...</p>
</article>
<article class="card c-line" style="left:113px;top:1520px">
  <svg viewBox="0 0 48 48" fill="#1f2326"><rect x="6" y="4" width="36" height="28" rx="3"/><rect x="2" y="36" width="44" height="8" rx="2"/><text x="24" y="24" font-size="16" font-family="Mulish,sans-serif" fill="#fff" text-anchor="middle">?</text></svg>
  <h3>Hardware Reparation</h3>
  <p>Nor again is there anyone who loves or pursues or desires to obtain pain of itself because it is pain, but because occasionally circumstances occur in which toil...</p>
</article>
<article class="card c-navy" style="left:447px;top:1520px">
  <svg viewBox="0 0 48 48" fill="none" stroke="#fff" stroke-width="2"><circle cx="24" cy="8" r="5"/><circle cx="10" cy="16" r="4"/><circle cx="38" cy="16" r="4"/><path d="M4 28h40M8 28v16M40 28v16M18 28v-8h12v8M14 44v-10M34 44v-10"/></svg>
  <h3>Consulting</h3>
  <p>Nor again is there anyone who loves or pursues or desires to obtain pain of itself because it is pain, but because occasionally circumstances occur in which toil...</p>
</article>
<article class="card c-teal" style="left:780px;top:1520px">
  <svg viewBox="0 0 48 48" fill="none" stroke="#fff" stroke-width="2"><rect x="18" y="4" width="26" height="18" rx="2"/><rect x="4" y="20" width="24" height="16" rx="2"/><path d="M16 36v6M10 42h12M31 22v6h-3"/></svg>
  <h3>Network Design</h3>
  <p>Nor again is there anyone who loves or pursues or desires to obtain pain of itself because it is pain, but because occasionally circumstances occur in which toil...</p>
</article>

<!-- CONSULTING -->
<section class="abs consult"></section>
<div class="abs serif label" style="left:113px;top:1925px">Professional</div>
<h2 class="abs h2" style="left:113px;top:1950px;color:var(--white);font-size:44px;line-height:44px">IT SERVICES<br>&amp; CONSULTING</h2>
<p class="abs para" style="left:113px;top:2055px;width:470px;color:#e6ebee">Nemo enim ipsam voluptatem quia voluptas sit aspernatur aut odit aut fugit, sed quia consequuntur magni dolores eos qui ratione voluptatem sequi nesciunt. Neque porro quisquam est, qui dolorem ipsum quia dolor sit amet, consectetur, adipisci velit, sed quia non numquam</p>
<div class="btn" style="left:113px;top:2191px;width:125px;height:42px">READ MORE</div>
<svg class="abs" style="left:596px;top:1883px;width:491px;height:396px" viewBox="0 0 491 396" role="img" aria-label="Photo of two businessmen looking at a tablet, cut into a rotated square">
  <defs>
    <linearGradient id="cp" x1="0" y1="0" x2="1" y2="1">
      <stop offset="0" stop-color="#a98c6c"/><stop offset=".45" stop-color="#3d4f66"/><stop offset="1" stop-color="#cfd6de"/>
    </linearGradient>
  </defs>
  <polygon points="40,180 180,0 490,200 330,396" fill="url(#cp)"/>
  <line x1="330" y1="80" x2="150" y2="350" stroke="#fff" stroke-width="3"/>
  <line x1="420" y1="140" x2="250" y2="380" stroke="#fff" stroke-width="3"/>
</svg>

<!-- TESTIMONIALS -->
<div class="abs center serif label" style="top:2372px">Testimonials</div>
<h2 class="abs center h2" style="top:2397px">PEOPLE ARE SAYING</h2>

<article class="quote q-blue" style="left:113px;top:2469px">
  <svg width="32" height="24" viewBox="0 0 32 24" fill="#fff"><path d="M0 0h13v12l-6 12H2l5-11H0zM18 0h13v12l-6 12h-5l5-11h-7z"/></svg>
  <p>Sed ut perspiciatis unde omnis iste natus error sit voluptatem accusantium doloremque laudantium, totam rem aperiam, eaque ipsa quae ab illo inventore veritatis et quasi architecto beatae vitae dicta sunt explicabo. Nemo enim ipsam voluptatem quia voluptas sit aspernatur aut odit aut fugit</p>
  <h4>Mr. Tomas Reiner</h4><small>Consultant</small>
</article>
<article class="quote q-pale" style="left:613px;top:2469px">
  <svg width="32" height="24" viewBox="0 0 32 24" fill="#1f2326"><path d="M0 0h13v12l-6 12H2l5-11H0zM18 0h13v12l-6 12h-5l5-11h-7z"/></svg>
  <p>Sed ut perspiciatis unde omnis iste natus error sit voluptatem accusantium doloremque laudantium, totam rem aperiam, eaque ipsa quae ab illo inventore veritatis et quasi architecto beatae vitae dicta sunt explicabo. Nemo enim ipsam voluptatem quia voluptas sit aspernatur aut odit aut fugit</p>
  <h4>Mr. Owen Castell</h4><small>Consultant</small>
</article>
<article class="quote q-line" style="left:113px;top:2762px">
  <svg width="32" height="24" viewBox="0 0 32 24" fill="#1f2326"><path d="M0 0h13v12l-6 12H2l5-11H0zM18 0h13v12l-6 12h-5l5-11h-7z"/></svg>
  <p>Sed ut perspiciatis unde omnis iste natus error sit voluptatem accusantium doloremque laudantium, totam rem aperiam, eaque ipsa quae ab illo inventore veritatis et quasi architecto beatae vitae dicta sunt explicabo. Nemo enim ipsam voluptatem quia voluptas sit aspernatur aut odit aut fugit</p>
  <h4>Mr. Elias Brandt</h4><small>Consultant</small>
</article>
<article class="quote q-royal" style="left:613px;top:2762px">
  <svg width="32" height="24" viewBox="0 0 32 24" fill="#fff"><path d="M0 0h13v12l-6 12H2l5-11H0zM18 0h13v12l-6 12h-5l5-11h-7z"/></svg>
  <p>Sed ut perspiciatis unde omnis iste natus error sit voluptatem accusantium doloremque laudantium, totam rem aperiam, eaque ipsa quae ab illo inventore veritatis et quasi architecto beatae vitae dicta sunt explicabo. Nemo enim ipsam voluptatem quia voluptas sit aspernatur aut odit aut fugit</p>
  <h4>Ms. Nadia Ferro</h4><small>Consultant</small>
</article>

<!-- CONTACT -->
<section class="abs contact"></section>
<h2 class="abs center h2" style="top:3155px;color:var(--white);font-size:44px">SEND US A MESSAGE</h2>
<p class="abs center" style="top:3205px;color:#e3ebf0;font-size:14px">Sed ut perspiciatis unde omnis iste natus error sit voluptatem accusantium</p>
<div class="field" style="left:232px;top:3247px;width:242px;height:40px">Name:</div>
<div class="field" style="left:478px;top:3247px;width:242px;height:40px">Email:</div>
<div class="field" style="left:726px;top:3247px;width:241px;height:40px">Phone:</div>
<div class="field" style="left:232px;top:3294px;width:735px;height:94px">Message:</div>
<div class="btn" style="left:851px;top:3397px;width:118px;height:40px;background:var(--bright);font-weight:600">SUBMIT</div>

<!-- FOOTER -->
<footer class="abs footer"></footer>
<h4 class="f-head serif" style="left:112px">Quick Links</h4>
<ul class="f-list" style="left:112px"><li>Home</li><li>Company</li><li>Services</li><li>Contact Us</li></ul>
<h4 class="f-head serif" style="left:362px">Services</h4>
<ul class="f-list" style="left:362px"><li>Software installation</li><li>Boost up your system</li><li>Hardware reparation</li><li>Consulting</li><li>Cloud Service</li><li>Network Design</li></ul>
<h4 class="f-head serif" style="left:644px">Contacts</h4>
<div class="f-contact" style="top:3598px"><svg width="10" height="14" viewBox="0 0 10 14" fill="#0a8bc8"><path d="M5 0a5 5 0 0 1 5 5c0 4-5 9-5 9S0 9 0 5a5 5 0 0 1 5-5z"/><circle cx="5" cy="5" r="2" fill="#f3f6f9"/></svg><span>Level 9, 14 Quay Street, Portwell,<br>Harbourside 4100, Northland</span></div>
<div class="f-contact" style="top:3659px"><svg width="10" height="14" viewBox="0 0 10 14" fill="#0a8bc8"><path d="M1 1l3-1 2 4-2 1c0 2 2 5 3 5l1-2 2 2-1 3C4 13 0 6 1 1z"/></svg><span>+00 (0) 555 014 729</span></div>
<div class="f-contact" style="top:3702px"><svg width="12" height="10" viewBox="0 0 12 10" fill="#0a8bc8"><rect width="12" height="10" rx="1"/><path d="M0 1l6 4 6-4" stroke="#f3f6f9" fill="none"/></svg><span>info@brightharbor.example</span></div>
<h4 class="f-head serif" style="left:988px">Follow Us</h4>
<div class="social" style="top:3599px"><i></i>Facepage</div>
<div class="social" style="top:3638px"><i></i>Chirper</div>
<div class="social" style="top:3677px"><i></i>Worknet</div>
<div class="abs center" style="top:3770px;font:700 12px 'Raleway',sans-serif;color:var(--bright);letter-spacing:1px">BRIGHT HARBOR</div>
<p class="abs center" style="top:3798px;font-size:11px;color:var(--ink)">COPYRIGHT © 2021 <span style="color:var(--blue)">BRIGHT HARBOR</span>. ALL RIGHTS RESERVED.</p>
<p class="abs center" style="top:3819px;font-size:9px;font-weight:700;color:var(--navy)">TERMS &amp; CONDITION I PRIVACY POLICY</p>

</body>
</html>
```